Independent horror publisher needs new web site

Hollow Lantern Books requires a new web site. We are an established independent publisher of horror fiction located in Melbourne, Australia. The publishing industry is undergoing radical changes with the advent of self publication and the new website has to address this issue by attracting future Authors. It needs to be easy to navigate, with a clean, modern style completely devoid of comedic/cheesy stereotypical horror garb. We have had a new logo (attached) designed recently and would like that to used as the main inspiration for the web site. Whilst our current website should not be used as either a practical or stylistic template, feel free to make use of our book covers. (www.hollowlanternbooks.example)
Updates
The font on our logo is Brandon Grotesque
Target Market(s)
The target market is authors - as such it cannot be grouped by age, gender, ethinicity etc.
Industry/Entity Type
Industry
Requirements
Must have
- On the front page we need a section where we can post latest news. Links to E-book and Paper stores, Submissions Page, About Us Page, Contact Us Page, forum and games page. Facebook Like and Twitter follow buttons.
Should not have
- Cheesy horror themes and fonts.

```html
<!DOCTYPE html>
<html lang="en">
<head>
<meta charset="utf-8">
<title>Hollow Lantern Books</title>
<link rel="stylesheet" href="https://fonts.googleapis.com/css2?family=Source+Sans+3:wght@400;600&display=swap">
<style>
:root{
  --accent:#e4572a;
  --ink:#1d1d1d;
  --body:#2a2a2a;
  --muted:#555;
  --nav:#474747;
  --nav-dark:#333;
  --line:#d9d9d9;
  --panel:#fafafa;
  --search:#f7931e;
  --btn:#3b3b3b;
  --social-a:#4fb3e8;
  --social-b:#3b5e9e;
}
*{box-sizing:border-box;margin:0;padding:0}
html,body{width:1180px;height:1200px;overflow:hidden}
body{position:relative;background:#fff;font-family:"Source Sans 3",sans-serif;color:var(--body)}
a{color:inherit;text-decoration:none}
.site-header{position:absolute;left:0;top:0;width:1180px;height:122px;background:linear-gradient(#fff,#efefef)}
.brand{position:absolute;left:152px;top:44px;display:flex;align-items:center;gap:10px}
.brand-mark{width:40px;height:40px;border-radius:50%;background:var(--ink)}
.brand-name{font-size:33px;font-weight:400;color:var(--ink);letter-spacing:.5px}
.follow{position:absolute;left:940px;top:32px;width:100px;text-align:center;font-size:13px;color:var(--ink)}
.follow-icons{display:flex;gap:12px;justify-content:center;margin-top:8px}
.social{width:33px;height:33px;border-radius:6px}
.social-a{background:var(--social-a)}
.social-b{background:var(--social-b)}
.main-nav{position:absolute;left:0;top:122px;width:1180px;height:38px;background:linear-gradient(var(--nav),var(--nav-dark));border-top:2px solid #6a6a6a}
.main-nav a{position:absolute;top:10px;font-size:13px;color:#fff}
.search{position:absolute;left:755px;top:6px;display:flex;gap:10px}
.search-field{width:172px;height:24px;background:#fff;border:1px solid #ccc}
.search-btn{width:89px;height:25px;background:var(--search);display:flex;align-items:center;font-size:13px;color:var(--ink);padding-left:11px;gap:14px}
.search-btn svg{border-left:1px solid #c06a10;padding-left:6px}
.hero{position:absolute;left:129px;top:179px;width:918px;height:322px;border:4px solid #fff;box-shadow:0 0 0 1px #ddd,0 8px 6px -4px rgba(0,0,0,.45);background:linear-gradient(90deg,#5a6a4c,#c9a271 30%,#e2c79a 55%,#b58f5c 80%,#6f7a5c)}
.dots{position:absolute;right:26px;bottom:8px;display:flex;gap:4px}
.dots i{width:10px;height:10px;border-radius:50%;background:#fff;display:block}
.dots i.on{border:2px solid var(--accent)}
.panel-head{position:absolute;height:34px;background:var(--panel);border:1px solid var(--line);font-size:17px;color:var(--accent);padding:6px 12px;display:flex;align-items:center}
.news-head{left:129px;top:525px;width:256px}
.ebook-head{left:397px;top:525px;width:650px;justify-content:space-between}
.ebook-head span b{font-weight:400;color:var(--accent)}
.ebook-head span{color:var(--ink)}
.news{position:absolute;left:136px;top:578px;width:240px;list-style:none}
.news li{display:flex;gap:16px;margin-bottom:16px;font-size:11.5px;line-height:17px;color:var(--ink)}
.news .more{color:var(--accent);display:block;margin-top:3px}
.cal{flex:none;width:16px;height:14px;margin-top:2px}
.books{position:absolute;left:422px;top:581px;display:flex;list-style:none}
.book{width:132px;position:relative;height:224px}
.cover{width:83px;height:123px;display:block;margin-left:1px}
.book h3{font-weight:400;font-size:14px;line-height:18px;color:var(--accent);margin-top:12px;width:100px}
.price{font-size:13.5px;color:var(--ink);margin-top:4px}
.read-more{position:absolute;left:1px;top:202px;width:84px;height:20px;background:var(--btn);color:#fff;font-size:11px;display:flex;align-items:center;justify-content:center}
.welcome-head{left:129px;top:833px;width:918px;font-size:17px}
.welcome{position:absolute;left:141px;top:886px;width:610px;font-size:11.8px;line-height:21.6px;color:var(--ink)}
.meeting{position:absolute;left:783px;top:872px;width:243px;height:170px;background:linear-gradient(135deg,#f4f4f4,#d9d2c8 45%,#2b2b30 70%,#eaeaea)}
.site-footer{position:absolute;left:0;top:1085px;width:1180px;height:115px;border-top:1px solid #e2e2e2;background:linear-gradient(#fff,#efefef);text-align:center}
.foot-nav{margin-top:35px;font-size:12.5px;color:var(--muted)}
.foot-nav a{padding:0 6px}
.copy{margin-top:8px;font-size:12px;color:var(--muted)}
</style>
</head>
<body>
<header class="site-header">
  <div class="brand"><span class="brand-mark"></span><span class="brand-name">HOLLOW LANTERN BOOKS</span></div>
  <div class="follow">Follow Us On
    <div class="follow-icons">
      <a class="social social-a" href="#" aria-label="Follow us"></a>
      <a class="social social-b" href="#" aria-label="Like us"></a>
    </div>
  </div>
</header>
<nav class="main-nav">
  <a href="#" style="left:147px">Home</a>
  <a href="#" style="left:213px">About Us</a>
  <a href="#" style="left:295px">Submissions</a>
  <a href="#" style="left:394px">Contact Us</a>
  <a href="#" style="left:487px">Forums</a>
  <a href="#" style="left:566px">Games</a>
  <a href="#" style="left:635px">Stores</a>
  <div class="search">
    <div class="search-field"></div>
    <div class="search-btn">Search
      <svg width="22" height="18" viewBox="0 0 22 18"><circle cx="12" cy="7" r="4.5" fill="none" stroke="#222" stroke-width="2"/><line x1="15" y1="10" x2="19" y2="15" stroke="#222" stroke-width="2.5"/></svg>
    </div>
  </div>
</nav>
<section class="hero" role="img" aria-label="Open old books lying on a table in front of shelves">
  <div class="dots"><i class="on"></i><i></i><i></i><i></i><i></i></div>
</section>
<div class="panel-head news-head">News</div>
<ul class="news">
  <li><svg class="cal" viewBox="0 0 16 14"><rect x="1" y="2" width="14" height="11" fill="#eee" stroke="#777"/><rect x="1" y="2" width="14" height="3" fill="#888"/></svg><div>Today I tried to persuade a local book store to carry Hollow Lantern books but ...<a class="more" href="#">Read More</a></div></li>
  <li><svg class="cal" viewBox="0 0 16 14"><rect x="1" y="2" width="14" height="11" fill="#eee" stroke="#777"/><rect x="1" y="2" width="14" height="3" fill="#888"/></svg><div>Today I tried to persuade a local book store to carry Hollow Lantern books but ...<a class="more" href="#">Read More</a></div></li>
  <li><svg class="cal" viewBox="0 0 16 14"><rect x="1" y="2" width="14" height="11" fill="#eee" stroke="#777"/><rect x="1" y="2" width="14" height="3" fill="#888"/></svg><div>Today I tried to persuade a local book store to carry Hollow Lantern books but ...<a class="more" href="#">Read More</a></div></li>
</ul>
<div class="panel-head ebook-head"><span><b>e</b> - book</span>
  <svg width="34" height="14" viewBox="0 0 34 14"><path d="M8 2 3 7l5 5M26 2l5 5-5 5" fill="none" stroke="#222" stroke-width="2"/></svg>
</div>
<ul class="books">
  <li class="book"><span class="cover" role="img" aria-label="Book cover: Ashfall Hour" style="background:linear-gradient(#bca578,#9c7a4e)"></span><h3>Ashfall Hour</h3><p class="price">$13.50</p><a class="read-more" href="#">Read More&nbsp;&nbsp;+</a></li>
  <li class="book"><span class="cover" role="img" aria-label="Book cover: The Quiet Accord" style="background:linear-gradient(#c2512c,#8a2a18)"></span><h3>The Quiet Accord</h3><p class="price">$7.99</p><a class="read-more" href="#">Read More&nbsp;&nbsp;+</a></li>
  <li class="book"><span class="cover" role="img" aria-label="Book cover: The Ember Season" style="background:linear-gradient(#2a0b0b,#7a1a14)"></span><h3>The Ember Season</h3><p class="price">$13.50</p><a class="read-more" href="#">Read More&nbsp;&nbsp;+</a></li>
  <li class="book"><span class="cover" role="img" aria-label="Book cover: Riders of the Dust" style="background:linear-gradient(#a08a74,#5a3e2c)"></span><h3>Riders of the Dust</h3><p class="price">$7.99</p><a class="read-more" href="#">Read More&nbsp;&nbsp;+</a></li>
  <li class="book"><span class="cover" role="img" aria-label="Book cover: Marrow: A Night Novel" style="background:linear-gradient(#b79a86,#6e5a4a)"></span><h3>Marrow: A Night Novel</h3><p class="price">$13.50</p><a class="read-more" href="#">Read More&nbsp;&nbsp;+</a></li>
</ul>
<div class="panel-head welcome-head">Welcome to our site</div>
<p class="welcome">Hollow Lantern Books will evaluate your work for entertainment, literary quality, and commercial appeal. Once our review process is complete we will either make you an offer to publish, decline to publish, or request that changes be made and the work resubmitted.Royalties are paid on every sale with the exception of author copies. Royalties are paid on a quarterly basis within 90 days of the end of each calendar quarter. Books are not considered sold, and royalties will not be paid, until payment is actually received by Hollow Lantern Books. Specific royalty percentages will be discussed if Hollow Lantern Books makes an offer to publish your book.</p>
<div class="meeting" role="img" aria-label="Photo of an author and a publisher shaking hands across a desk"></div>
<footer class="site-footer">
  <nav class="foot-nav"><a href="#">Home</a>|<a href="#">About Us</a>|<a href="#">Submissions</a>|<a href="#">Contact Us</a>|<a href="#">Forums</a>|<a href="#">Games</a>|<a href="#">Stores</a></nav>
  <p class="copy">Copyrights @ 2012 All Rights Reserved</p>
</footer>
</body>
</html>
```